Vehicle Signage Design for a Renovation Company

We're a renovation company specialising in Home Renovations. The final design should communicate trust, credibility, and confidence. We need vehicle signage designed for our company utes (see attachment) / for our grey ute with the canopy/ and white use withou the canopyI've also attached our existing designs for the current vehicles (van and hatch back) to give you an idea of what we're after.In terms of content, there isn't much requirement for this due to the limited space on the ute - but happy to hear ideas on this.We've tried designing it ourselves - see attachment, but not happy with the result, would like more variations and ideas.Check out our website www.kestrelrenovations.co.nz for ideas on our branding/ style.
Updates

Target Market(s)

Home Owners

Industry/Entity Type

Residential Construction

Font styles to use
Sans Serif

Colors
3276b5
0355a3
33a6d7
3aa7d7
ffffff

Requirements
Must have
• Logo, Call to Action (website and number), Headline
Nice to have
• Strong sharp lines, a clean/sleek look
• It would be nice to have our offer on there (free design plans) / but we know space is limited

```html
<!DOCTYPE html>
<html lang="en">
<head>
<meta charset="utf-8">
<title>Kestrel Home Renovations – Ute Side Signage</title>
<link rel="stylesheet" href="https://fonts.googleapis.com/css2?family=Hind:wght@400;500;600&family=Montserrat:wght@700&display=swap">
<style>
  :root {
    --brand-deep: #0355a3;
    --brand-mid: #3276b5;
    --brand-sky: #33a6d7;
    --brand-sky-alt: #3aa7d7;
    --brand-white: #ffffff;
    --panel-silver: #eef1f4;
    --page: #ffffff;
  }

  html, body {
    margin: 0;
    padding: 0;
    width: 1200px;
    height: 790px;
    overflow: hidden;
    background: var(--page);
  }

  .signage {
    position: relative;
    width: 1200px;
    height: 790px;
    overflow: hidden;
    background: var(--panel-silver);
    font-family: "Hind", sans-serif;
  }

  .signage__panels {
    position: absolute;
    inset: 0;
  }

  /* Door panel – logo */
  .logo {
    position: absolute;
    left: 96px;
    top: 250px;
    margin: 0;
    color: var(--brand-sky-alt);
    font-family: "Montserrat", sans-serif;
    font-weight: 700;
    line-height: 1;
  }
  .logo__name {
    display: block;
    font-size: 104px;
    letter-spacing: -1px;
  }
  .logo__tagline {
    display: block;
    margin: 14px 0 0 150px;
    font-size: 26px;
    letter-spacing: 1px;
  }

  /* Illustrations */
  .illustration {
    position: absolute;
  }
  .illustration--fence-trees {
    left: 40px;
    top: 520px;
    width: 230px;
    height: 270px;
    background: linear-gradient(180deg, var(--brand-mid) 0%, var(--brand-sky) 100%);
    border-radius: 110px 110px 0 0;
  }
  .illustration--house {
    left: 420px;
    top: 420px;
    width: 220px;
    height: 370px;
    background: linear-gradient(180deg, var(--brand-mid) 0%, var(--brand-sky) 100%);
  }
  .illustration--foliage {
    left: 560px;
    top: 150px;
    width: 170px;
    height: 640px;
    background: linear-gradient(180deg, rgba(255,255,255,0.15) 0%, rgba(255,255,255,0.35) 100%);
    border-radius: 85px 85px 0 0;
  }

  /* Tub panel – call to action */
  .cta {
    position: absolute;
    left: 752px;
    top: 252px;
    width: 420px;
    color: var(--brand-white);
  }
  .cta__headline {
    margin: 0;
    font-weight: 600;
    font-size: 34px;
    line-height: 1.05;
    white-space: nowrap;
  }
  .cta__offer {
    margin: 14px 0 0 132px;
    font-weight: 400;
    font-size: 16px;
    line-height: 1.2;
    opacity: 0.9;
  }
  .cta__phone {
    margin: 4px 0 0 132px;
    font-weight: 600;
    font-size: 36px;
    letter-spacing: 1px;
    line-height: 1;
  }
  .cta__web {
    margin: 10px 0 0 132px;
    font-weight: 500;
    font-size: 17px;
    line-height: 1.2;
    white-space: nowrap;
  }
</style>
</head>
<body>
  <main class="signage">
    <svg class="signage__panels" width="1200" height="790" viewBox="0 0 1200 790" aria-hidden="true">
      <defs>
        <linearGradient id="tubGradient" x1="0" y1="0" x2="1" y2="0">
          <stop offset="0" stop-color="#33a6d7"/>
          <stop offset="1" stop-color="#3276b5"/>
        </linearGradient>
      </defs>
      <polygon points="700,0 1200,0 1200,790 620,790" fill="url(#tubGradient)"/>
    </svg>

    <h1 class="logo">
      <span class="logo__name">Kestrel</span>
      <span class="logo__tagline">HOME RENOVATIONS</span>
    </h1>

    <div class="illustration illustration--fence-trees" role="img" aria-label="Illustration of a picket fence with two leafy trees in blue tones"></div>
    <div class="illustration illustration--house" role="img" aria-label="Illustration of a simple blue house with a window, set among rounded shrubs"></div>
    <div class="illustration illustration--foliage" role="img" aria-label="Decorative pale blue leaf shapes along the edge of the blue panel"></div>

    <section class="cta">
      <h2 class="cta__headline">Thinking about Renovating?</h2>
      <p class="cta__offer">Design to build Consultation</p>
      <p class="cta__phone">0800 555 014</p>
      <p class="cta__web">www.kestrelrenovations.co.nz</p>
    </section>
  </main>
</body>
</html>
```